Lumara Health & Wellness Business Card Design

We would like to create business cards matching with our new logo design. The card should be professional looking but still have a playful side and something that would be eye catching. We are planing to open a luxury medical spa and looking to create a design based on this new logo. We are looking for a design that shows off luxury but not be gold in color. Also, while we are a more female oriented medical center we do have men that come in for our services and it should be be too feminine.

Target Market(s)

Health & Wellness. Medical patients. Luxury spa

Industry/Entity Type

Health And Wellness

Contact Information for Business Card

It should have the logo design in the front of card and back of card should have our contact information. Our current colors are peach/ coral, teal, and gray. We are looking for a modern looking design.

Font styles to use
Script

Colors
32a6d6
e667a6
86cfc6
fece3e

Requirements
Must have
• It should have our logo design. We would prefer to have a more modern look to the card.
Nice to have
• Eye-Catching Design on the personable side but still classy.
Should not have
• At this point we are looking for the best design. It should not have color purple.

```html
<!DOCTYPE html>
<html lang="en">
<head>
<meta charset="utf-8">
<title>Lumara Health &amp; Wellness — Business Card</title>
<link href="https://fonts.googleapis.com/css2?family=Libre+Baskerville:ital@0;1&display=swap" rel="stylesheet">
<style>
  :root {
    --stage: #dde1e4;
    --paper: #ffffff;
    --ink: #111111;
    --sun: #fece3e;
    --mint: #86cfc6;
    --rose: #e667a6;
  }
  html, body {
    margin: 0;
    padding: 0;
    width: 1200px;
    height: 1200px;
    overflow: hidden;
    background: var(--stage);
  }
  .canvas {
    position: relative;
    width: 1200px;
    height: 1200px;
  }
  .card {
    position: absolute;
    left: 141px;
    width: 911px;
    background: var(--paper);
    overflow: hidden;
  }
  .card-front { top: 65px; height: 520px; }
  .card-back { top: 630px; height: 518px; }

  .brush-field {
    position: absolute;
    inset: 0;
    background: linear-gradient(180deg,
      var(--sun) 0%, var(--sun) 26%,
      var(--mint) 40%, var(--mint) 52%,
      var(--rose) 66%, var(--rose) 100%);
  }
  .name-panel {
    position: absolute;
    left: 209px;
    top: 124px;
    width: 501px;
    height: 219px;
    background: var(--paper);
    display: flex;
    align-items: center;
    justify-content: center;
  }
  .brand-name {
    font-family: "Libre Baskerville", Georgia, serif;
    font-weight: 400;
    font-style: normal;
    color: var(--ink);
    font-size: 30px;
    letter-spacing: 0.5px;
    margin: 0;
    white-space: nowrap;
  }
  .back-brand {
    position: absolute;
    left: 0;
    right: 0;
    top: 170px;
    text-align: center;
  }
  .contact {
    position: absolute;
    left: 0;
    right: 0;
    top: 340px;
    margin: 0;
    padding: 0;
    list-style: none;
    text-align: center;
    font-family: "Libre Baskerville", Georgia, serif;
    font-style: italic;
    font-size: 20px;
    line-height: 28.5px;
    color: var(--ink);
  }
</style>
</head>
<body>
<main class="canvas">
  <section class="card card-front">
    <div class="brush-field" role="img" aria-label="Painted brush strokes in yellow, teal and pink"></div>
    <div class="name-panel">
      <p class="brand-name">Lumara Health &amp; Wellness</p>
    </div>
  </section>

  <section class="card card-back">
    <div class="back-brand">
      <p class="brand-name">Lumara Health &amp; Wellness</p>
    </div>
    <ul class="contact">
      <li>(555) 014-2280</li>
      <li>hello@lumarawellness.com</li>
      <li>42 Linden Ave, Suite 4 Fairview, NJ 07000</li>
      <li>www.lumarawellness.com</li>
    </ul>
  </section>
</main>
</body>
</html>
```